Halvek Insurance Stationery Design Project

We need a stationery design for business cards, letterhead and envelopes.

Please refer to attached brief for further information.

Business

```html
<!DOCTYPE html>
<html lang="en">
<head>
<meta charset="utf-8">
<title>Halvek Insurance Stationery</title>
<link href="https://fonts.googleapis.com/css2?family=Barlow:wght@400;500;600&display=swap" rel="stylesheet">
<style>
:root{
  --blue:#0d62b5;
  --blue-dark:#0a3d7a;
  --blue-light:#2f93e6;
  --paper:#ffffff;
  --paper-shade:#eef1f5;
  --ink:#2b2b2b;
  --muted:#8a8f96;
  --stage:#e4e6ea;
}
*{box-sizing:border-box;margin:0;padding:0}
html,body{width:1200px;height:848px;overflow:hidden}
body{background:var(--stage);font-family:"Barlow",Arial,sans-serif;color:var(--ink);position:relative}
address{font-style:normal}
.piece{position:absolute;background:var(--paper);box-shadow:0 4px 14px rgba(0,0,0,.18);overflow:hidden}
.band{position:absolute;left:0;top:0;width:100%;background:linear-gradient(180deg,var(--blue-light),var(--blue) 55%,var(--blue-dark));border-bottom:3px solid #c9ced6}
.brand{position:absolute;display:flex;align-items:center;gap:8px;color:#fff;font-weight:600;white-space:nowrap}
.brand-dot{width:12px;height:12px;border-radius:50%;background:#fff;flex:none}
.address{position:absolute;right:18px;color:#fff;font-size:10px;line-height:1.35;text-align:right}
.url{position:absolute;font-size:9px;color:var(--muted)}
.corner{position:absolute;right:0;bottom:14px;width:40px;height:6px;background:var(--blue)}

/* letterhead */
.letterhead{left:40px;top:40px;width:420px;height:594px}
.letterhead .band{height:92px}
.letterhead .brand{left:22px;top:18px;font-size:22px}
.letterhead .address{top:16px}
.letter-body{position:absolute;left:40px;right:36px;top:122px;font-size:9.5px;line-height:1.5}
.letter-body p{margin-bottom:10px}
.letter-body ul{list-style:none;margin:0 0 10px 10px}
.letter-body li::before{content:"+";margin-right:10px}
.signature{width:110px;height:26px;background:#f1f2f4;border-radius:3px;margin:6px 0 6px}
.letterhead .url{right:56px;bottom:18px}

/* envelope front */
.envelope{left:490px;top:40px;width:360px;height:190px}
.envelope .band{height:62px}
.envelope .brand{left:18px;top:12px;font-size:18px}
.envelope .address{top:70px;color:var(--ink);font-size:9px}
.envelope .url{right:48px;bottom:16px}

/* envelope back */
.envelope-back{left:490px;top:250px;width:360px;height:190px;background:var(--paper-shade)}
.envelope-back svg{position:absolute;inset:0}
.envelope-back .brand{left:50%;top:62px;transform:translateX(-50%);color:var(--blue-dark);font-size:16px}
.envelope-back .brand-dot{background:var(--blue-dark)}

/* folder */
.folder{left:880px;top:40px;width:280px;height:400px;border-radius:10px;background:radial-gradient(circle at 55% 40%,var(--blue-light),var(--blue) 45%,var(--blue-dark))}
.folder .brand{left:50%;top:170px;transform:translateX(-50%);font-size:24px}
.folder .url{left:0;right:0;bottom:22px;text-align:center;color:#fff;font-size:10px;font-weight:500}

/* business card */
.card{left:490px;top:470px;width:340px;height:195px;border-radius:10px}
.card .band{height:92px}
.card-name{position:absolute;left:18px;top:16px;color:#fff;font-size:13px;font-weight:600}
.card-title{position:absolute;left:18px;top:34px;color:#dbe8f7;font-size:8px}
.card .brand{right:16px;top:56px;font-size:19px;color:#fff}
.card-address{position:absolute;left:18px;top:110px;font-size:8px;line-height:1.4}
.card-contacts{position:absolute;left:168px;top:110px;font-size:8px;line-height:1.5;list-style:none}
.card-contacts svg{width:8px;height:8px;vertical-align:-1px;margin-right:4px}
</style>
</head>
<body>

<section class="piece letterhead" aria-label="Letterhead">
  <div class="band">
    <div class="brand"><span class="brand-dot"></span>Halvek Insurance</div>
    <address class="address">218 Harlow Street, 9th Floor,<br>Brookfield, NY 10031<br>&#9990; : 212-555-0147<br>www.halvekinsurance.com</address>
  </div>
  <div class="letter-body">
    <p>Dear Mr. First Last</p>
    <p>An henismod et wismod magnim eugue molore do dolobor si te consecte dolenim deliquis alisit esequipit wisl iure velis nim vulla odo od eu faccum il ullamconse facipis augiamc onullaorem volore ing eugiamet, quis at nim iure dunt duis nos auguera tueriure dolor nonsectem do consequisi bla feum eum volortin eu feu feugue tat iuscillaore dolore venim adipsummy niat wisl ulput in utpat, volore odolorem ad duis nosto conummy nis alit la adiatum ad eriusto.</p>
    <p>Qualifications:</p>
    <ul><li>adsf asdf sadf</li><li>asdf asd fasdf asdf</li><li>asdf asdf asdf asdf</li></ul>
    <p>Raestie corperat adiam quat. Raestrud ea feugait iuscipit adit lan eugiatin hendre ing eugait dolore dolobor augiam eugiam, quam, qui enit wisit pratem am, se do commodolum vel dolorem num aliqui bla feum in ullaore velis atisl et praessed andrero dolum etum quisit nonsequam dolessi tet duis niaturat. Dio odionullam dolor sustrud ercip eraestrud tatem venit augiat ilisit velis ad do odiate te dionsecte.</p>
    <p>Sincerely,</p>
    <div class="signature" role="img" aria-label="Handwritten signature of Colin Ardway"></div>
    <p>Colin Ardway</p>
  </div>
  <span class="url">www.halvekinsurance.com</span>
  <span class="corner"></span>
</section>

<section class="piece envelope" aria-label="Envelope front">
  <div class="band">
    <div class="brand"><span class="brand-dot"></span>Halvek Insurance</div>
  </div>
  <address class="address">218 Harlow Street, 9th Floor,<br>Brookfield, NY 10031<br>&#9990; : 212-555-0147<br>www.halvekinsurance.com</address>
  <span class="url">www.halvekinsurance.com</span>
  <span class="corner"></span>
</section>

<section class="piece envelope-back" aria-label="Envelope back">
  <svg viewBox="0 0 360 190" preserveAspectRatio="none" aria-hidden="true">
    <path d="M0 0 H360 V70 C300 70 240 130 180 110 C120 92 60 60 0 50 Z" fill="#ffffff" stroke="#c9ced6" stroke-width="1"/>
  </svg>
  <div class="brand"><span class="brand-dot"></span>Halvek Insurance</div>
</section>

<section class="piece folder" aria-label="Presentation folder">
  <div class="brand"><span class="brand-dot"></span>Halvek Insurance</div>
  <span class="url">www.halvekinsurance.com</span>
</section>

<section class="piece card" aria-label="Business card">
  <div class="band">
    <div class="card-name">Marten Vosk</div>
    <div class="card-title">CEO</div>
  </div>
  <div class="brand"><span class="brand-dot"></span>Halvek Insurance</div>
  <address class="card-address">Vestergade 14, 2800 Lyngby<br>Danmark</address>
  <ul class="card-contacts">
    <li><svg viewBox="0 0 10 10"><path d="M2 1l2 2-1 1.5c.8 1.4 1.6 2.2 3 3L7.5 6l2 2-1.5 1.5C4.5 9.5.5 5.5.5 2.5z" fill="#333"/></svg>: 813-555-0192</li>
    <li><svg viewBox="0 0 10 10"><path d="M2 1l2 2-1 1.5c.8 1.4 1.6 2.2 3 3L7.5 6l2 2-1.5 1.5C4.5 9.5.5 5.5.5 2.5z" fill="#333"/></svg>: 1-877-555-0163</li>
    <li><svg viewBox="0 0 10 10"><rect x="0.5" y="2" width="9" height="6" fill="none" stroke="#333"/><path d="M.5 2l4.5 3.5L9.5 2" fill="none" stroke="#333"/></svg>: info@ridgefieldholdings.com</li>
    <li><svg viewBox="0 0 10 10"><circle cx="5" cy="5" r="4.2" fill="none" stroke="#333"/><path d="M1 5h8M5 .8v8.4" stroke="#333" fill="none"/></svg>: ridgefieldholdings.com</li>
  </ul>
</section>

</body>
</html>
```